Redesign Event Flyer for Speaker

We are re-designing our professional event flyer template with new headshot and cleaner, up-to-date design. All design details are in PDF file attached. Thank you for participating :)

Font styles to use
Sans Serif

Colors
3276b5
0355a3

Requirements
Must have
• All elements in PDF file.
Nice to have
Should not have
• Tacky or childish elements.

```html
<!DOCTYPE html>
<html lang="en">
<head>
<meta charset="utf-8">
<title>The Greatest Sale – Event Flyer</title>
<link href="https://fonts.googleapis.com/css2?family=Bebas+Neue&family=Cinzel:wght@400&family=Cabin:wght@400;500&display=swap" rel="stylesheet">
<style>
  :root {
    --page-bg: #ececec;
    --card-light: #6e6f73;
    --card-mid: #55565a;
    --card-dark: #3d3e42;
    --suit-navy: #26344f;
    --skin-tone: #6b4a3a;
    --shirt-white: #e9e9ea;
    --text-white: #ffffff;
    --text-soft: #e6e6e8;
    --brand-red: #d7282f;
  }
  * { margin: 0; padding: 0; box-sizing: border-box; }
  html, body {
    width: 1200px;
    height: 909px;
    overflow: hidden;
    background: var(--page-bg);
  }
  .flyer {
    position: absolute;
    left: 50px;
    top: 88px;
    width: 1100px;
    height: 733px;
    overflow: hidden;
    background: radial-gradient(ellipse at 38% 35%, var(--card-light) 0%, var(--card-mid) 45%, var(--card-dark) 100%);
    color: var(--text-white);
    font-family: "Cabin", "Helvetica Neue", Arial, sans-serif;
  }
  .speaker-photo {
    position: absolute;
    left: 46px;
    top: 51px;
    width: 561px;
    height: 682px;
  }
  .speaker-photo svg { display: block; width: 100%; height: 100%; }
  .headline-block {
    position: absolute;
    right: 65px;
    top: 150px;
    text-align: right;
  }
  .brand-name {
    display: inline-flex;
    align-items: center;
    gap: 10px;
    font-size: 34px;
    font-weight: 500;
    color: var(--brand-red);
    line-height: 1;
    margin-right: 10px;
  }
  .brand-mark {
    width: 22px;
    height: 22px;
    background: var(--brand-red);
  }
  .event-title {
    margin-top: 22px;
    font-family: "Bebas Neue", "Arial Narrow", sans-serif;
    font-weight: 400;
    font-size: 72px;
    line-height: 1;
    letter-spacing: 0.5px;
    color: var(--text-white);
  }
  .speaker-name {
    margin-top: 4px;
    font-family: "Cinzel", Georgia, serif;
    font-size: 25px;
    letter-spacing: 1px;
    color: var(--text-soft);
  }
  .venue-block {
    position: absolute;
    right: 65px;
    top: 470px;
    text-align: right;
  }
  .venue-name {
    display: inline-flex;
    align-items: center;
    gap: 10px;
    font-size: 15px;
    font-weight: 500;
    letter-spacing: 1.5px;
    text-transform: uppercase;
    color: var(--text-white);
    margin-right: 2px;
  }
  .venue-mark {
    width: 34px;
    height: 34px;
    border: 2px solid var(--text-white);
  }
  .event-details {
    margin-top: 54px;
    font-size: 20px;
    line-height: 31px;
    color: var(--text-soft);
  }
  .contact-links {
    position: absolute;
    right: 65px;
    top: 683px;
    font-size: 18px;
    letter-spacing: 0.6px;
    color: var(--text-soft);
  }
</style>
</head>
<body>
  <main class="flyer">
    <div class="speaker-photo" role="img" aria-label="Headshot of the speaker, smiling, in a navy blazer and white open-collar shirt">
      <svg viewBox="0 0 561 682" preserveAspectRatio="none">
        <defs>
          <radialGradient id="speakerTones" cx="50%" cy="35%" r="70%">
            <stop offset="0%" stop-color="var(--skin-tone)" stop-opacity="0.55"/>
            <stop offset="40%" stop-color="var(--suit-navy)" stop-opacity="0.75"/>
            <stop offset="100%" stop-color="var(--suit-navy)" stop-opacity="0"/>
          </radialGradient>
        </defs>
        <rect width="561" height="682" fill="url(#speakerTones)"/>
      </svg>
    </div>

    <header class="headline-block">
      <div class="brand-name"><span class="brand-mark"></span>Markwell Signs</div>
      <h1 class="event-title">The Greatest Sale</h1>
      <p class="speaker-name">Julian Marcus Bennett</p>
    </header>

    <section class="venue-block">
      <div class="venue-name"><span class="venue-mark"></span>Falling Ridge Golf Club</div>
      <p class="event-details">
        Friday, August 9th, 2019<br>
        4200 Lakeshore Pkwy, Port Alden, Canada
      </p>
    </section>

    <footer class="contact-links">julianmarcusbennett.com | markwellsigns.ca</footer>
  </main>
</body>
</html>
```